Quarlwick Builders Business Cards

I want to use the logo and make an unique business card that shows the textured Logo with brick and builings. I want to be able to stand out when I pass out business cards.

```html
<!DOCTYPE html>
<html lang="en">
<head>
<meta charset="utf-8">
<title>Quarlwick Builders Business Cards</title>
<link rel="stylesheet" href="https://fonts.googleapis.com/css2?family=Oswald:wght@500;700&family=Roboto+Condensed:wght@500&display=swap">
<style>
  :root {
    --page-bg: #d1d4d6;
    --card-light: #6b6b6b;
    --card-mid: #3a3a3a;
    --card-dark: #171717;
    --brick: #e2512f;
    --tagline: #1d2440;
    --tagline-glow: rgba(255,255,255,0.55);
    --scratch-dark: rgba(0,0,0,0.45);
    --scratch-light: rgba(255,255,255,0.12);
  }
  * { margin: 0; padding: 0; box-sizing: border-box; }
  html, body { width: 900px; height: 1200px; overflow: hidden; }
  body { background: var(--page-bg); position: relative; font-family: "Oswald", sans-serif; }

  .card {
    position: absolute;
    left: 136px;
    width: 630px;
    height: 357px;
    border-radius: 14px;
    overflow: hidden;
    background: radial-gradient(ellipse 65% 70% at 50% 45%, var(--card-light) 0%, var(--card-mid) 55%, var(--card-dark) 100%);
  }
  .card--front { top: 215px; }
  .card--back { top: 629px; background: radial-gradient(ellipse 70% 75% at 55% 45%, var(--card-light) 0%, var(--card-mid) 55%, var(--card-dark) 100%); }

  .grunge {
    position: absolute;
    inset: 0;
    width: 100%;
    height: 100%;
    pointer-events: none;
  }
  .grunge__spots {
    position: absolute;
    inset: 0;
    background:
      radial-gradient(circle at 12% 22%, rgba(0,0,0,0.25) 0 2px, transparent 3px),
      radial-gradient(circle at 78% 14%, rgba(0,0,0,0.22) 0 1.5px, transparent 3px),
      radial-gradient(circle at 88% 72%, rgba(0,0,0,0.25) 0 2px, transparent 3px),
      radial-gradient(circle at 30% 82%, rgba(0,0,0,0.2) 0 1.5px, transparent 3px),
      radial-gradient(ellipse 30% 20% at 20% 75%, rgba(0,0,0,0.18), transparent 70%),
      radial-gradient(ellipse 25% 22% at 85% 30%, rgba(0,0,0,0.15), transparent 70%),
      radial-gradient(ellipse 22% 18% at 65% 85%, rgba(255,255,255,0.05), transparent 70%);
  }
  .grunge path { fill: none; stroke-linecap: round; }
  .grunge .dark { stroke: var(--scratch-dark); stroke-width: 0.8; }
  .grunge .light { stroke: var(--scratch-light); stroke-width: 0.7; }

  .brand {
    position: absolute;
    display: flex;
    align-items: center;
    gap: 12px;
    color: var(--brick);
    font-family: "Oswald", sans-serif;
    font-weight: 700;
    text-transform: uppercase;
    white-space: nowrap;
  }
  .brand__mark { background: var(--brick); flex: none; }

  .card--front .brand { left: 0; right: 0; top: 120px; justify-content: center; font-size: 50px; letter-spacing: 1px; }
  .card--front .brand__mark { width: 30px; height: 30px; }

  .tagline {
    position: absolute;
    font-family: "Roboto Condensed", sans-serif;
    font-weight: 500;
    color: var(--tagline);
    text-shadow: 0 0 4px var(--tagline-glow), 0 0 8px var(--tagline-glow);
    white-space: nowrap;
  }
  .card--front .tagline { left: 0; right: 0; top: 305px; text-align: center; font-size: 16.5px; }

  .card--back .brand { left: 36px; top: 135px; font-size: 24px; gap: 8px; }
  .card--back .brand__mark { width: 16px; height: 16px; }
  .card--back .tagline {
    left: 180px;
    top: 255px;
    transform: translateX(-50%);
    font-size: 11px;
    letter-spacing: 0.1px;
    text-shadow: 0 0 2px rgba(255,255,255,0.85), 0 0 6px rgba(255,255,255,0.6);
  }

  .holder { position: absolute; left: 303px; top: 96px; color: var(--brick); }
  .holder__name { font-size: 36px; font-weight: 700; line-height: 1; letter-spacing: 0.3px; }
  .holder__role { margin-top: 8px; font-size: 15px; font-weight: 500; letter-spacing: 1px; }

  .contacts { position: absolute; left: 303px; top: 191px; list-style: none; color: var(--brick); }
  .contacts li { display: flex; align-items: center; gap: 6px; height: 26px; font-size: 17.5px; font-weight: 500; letter-spacing: 0.6px; text-transform: uppercase; }
  .contacts svg { width: 17px; height: 17px; flex: none; }
</style>
</head>
<body>

<section class="card card--front" aria-label="Business card front">
  <div class="grunge__spots"></div>
  <svg class="grunge" viewBox="0 0 630 357" aria-hidden="true">
    <path class="dark" d="M40 60 L95 48 M60 250 L120 300 M520 40 L590 70 M500 300 L560 280 M30 180 L48 230 M580 190 L600 240 M150 330 L210 320"/>
    <path class="light" d="M70 120 L130 95 M450 320 L510 335 M560 110 L610 130 M20 300 L80 290 M250 20 L300 35"/>
  </svg>
  <div class="brand"><span class="brand__mark"></span>Quarlwick Builders</div>
  <p class="tagline">Patios - Sidewalks - Retaining Walls - Foundations</p>
</section>

<section class="card card--back" aria-label="Business card back">
  <div class="grunge__spots"></div>
  <svg class="grunge" viewBox="0 0 630 357" aria-hidden="true">
    <path class="dark" d="M30 40 L90 30 M50 280 L110 320 M540 50 L600 80 M520 300 L590 285 M20 150 L35 200 M600 200 L615 250 M260 330 L320 318"/>
    <path class="light" d="M80 90 L140 70 M430 320 L490 338 M560 130 L612 150 M15 320 L70 308 M280 15 L330 30"/>
  </svg>
  <div class="brand"><span class="brand__mark"></span>Quarlwick Builders</div>
  <p class="tagline">Patios - Sidewalks - Retaining Walls - Foundations</p>

  <div class="holder">
    <h1 class="holder__name">DALE MORROW</h1>
    <p class="holder__role">OWNER</p>
  </div>

  <ul class="contacts">
    <li>
      <svg viewBox="0 0 24 24" aria-hidden="true"><path fill="var(--brick)" d="M6.6 10.8a15.1 15.1 0 0 0 6.6 6.6l2.2-2.2a1 1 0 0 1 1-.25 11.4 11.4 0 0 0 3.6.57 1 1 0 0 1 1 1V20a1 1 0 0 1-1 1A17 17 0 0 1 3 4a1 1 0 0 1 1-1h3.5a1 1 0 0 1 1 1c0 1.25.2 2.45.57 3.6a1 1 0 0 1-.25 1z"/></svg>
      (253) 555-0147
    </li>
    <li>
      <svg viewBox="0 0 24 24" aria-hidden="true"><rect x="2" y="5" width="20" height="14" fill="var(--brick)"/><path d="M3 6l9 7 9-7" fill="none" stroke="#2a2a2a" stroke-width="2"/></svg>
      info@quarlwickbuilders.com
    </li>
    <li>
      <svg viewBox="0 0 24 24" aria-hidden="true"><circle cx="12" cy="12" r="10" fill="var(--brick)"/><g fill="none" stroke="#2a2a2a" stroke-width="1.5"><ellipse cx="12" cy="12" rx="4" ry="10"/><path d="M2 12h20M4 7h16M4 17h16"/></g></svg>
      www.quarlwickbuilders.com
    </li>
  </ul>
</section>

</body>
</html>
```